Residential Remodeling Contractor needs updated business card

I need a new design for my business card.
Name of the company is Corvell Construction. I need a card that commands presence, strength, integrity. I have been in business for 28 years. I am a Residential Remodeling Contractor that covers all aspects of a residential remodel and build.

```html
<!DOCTYPE html>
<html lang="en">
<head>
<meta charset="utf-8">
<title>Corvell Construction – Business Card</title>
<link href="https://fonts.googleapis.com/css2?family=Montserrat:wght@400;500;600&family=Oswald:wght@600&display=swap" rel="stylesheet">
<style>
  :root {
    --brand-blue: #1f3c7e;
    --ink: #1c1c1c;
    --paper: #ffffff;
    --backdrop: #e4e4e4;
  }
  * { margin: 0; padding: 0; box-sizing: border-box; }
  html, body { width: 1200px; height: 801px; overflow: hidden; }
  body {
    background: var(--backdrop);
    font-family: "Montserrat", sans-serif;
    position: relative;
  }
  .card {
    position: absolute;
    top: 252px;
    width: 520px;
    height: 297px;
    box-shadow: 0 6px 18px rgba(0,0,0,0.18);
  }
  .card--front { left: 50px; background: var(--paper); }
  .card--back  { left: 630px; background: var(--brand-blue); }

  /* Wordmark */
  .wordmark {
    font-family: "Montserrat", sans-serif;
    font-weight: 600;
    text-transform: uppercase;
    letter-spacing: 0.04em;
    line-height: 1.1;
    display: flex;
    align-items: center;
    gap: 10px;
  }
  .wordmark__square { width: 14px; height: 14px; flex: none; }

  .card--front .wordmark {
    position: absolute;
    top: 44px; left: 0; right: 0;
    justify-content: center;
    color: var(--brand-blue);
    font-size: 22px;
  }
  .card--front .wordmark__square { background: var(--brand-blue); }

  .identity-row {
    position: absolute;
    top: 132px; left: 0; right: 0;
    display: flex;
    justify-content: center;
    align-items: center;
    gap: 18px;
  }
  .person { text-align: right; }
  .person__name {
    font-family: "Oswald", sans-serif;
    font-weight: 600;
    font-size: 34px;
    color: var(--brand-blue);
    text-transform: uppercase;
    letter-spacing: 0.01em;
    line-height: 1;
  }
  .person__title { font-size: 11px; color: var(--ink); margin-top: 4px; }
  .divider { width: 1px; height: 56px; background: var(--brand-blue); }
  .contacts { list-style: none; font-size: 11.5px; color: var(--ink); }
  .contacts li { display: flex; align-items: center; gap: 6px; line-height: 1.55; }
  .contacts svg { width: 10px; height: 10px; flex: none; }
  .contacts .web { color: var(--ink); }
  .contacts .web span { color: var(--brand-blue); }

  .address {
    position: absolute;
    bottom: 42px; left: 0; right: 0;
    text-align: center;
    font-size: 12px;
    color: var(--ink);
    letter-spacing: 0.02em;
  }

  .card--back .wordmark {
    position: absolute;
    top: 100px; left: 0; right: 0;
    justify-content: center;
    color: var(--paper);
    font-size: 28px;
  }
  .card--back .wordmark__square { background: var(--paper); width: 16px; height: 16px; }
  .tagline {
    position: absolute;
    bottom: 62px; left: 0; right: 0;
    text-align: center;
    color: var(--paper);
    font-weight: 600;
    font-size: 13px;
    letter-spacing: 0.12em;
    text-transform: uppercase;
  }
</style>
</head>
<body>
  <section class="card card--front" aria-label="Business card front">
    <div class="wordmark"><span class="wordmark__square"></span>Corvell Construction</div>

    <div class="identity-row">
      <div class="person">
        <div class="person__name">Marcus Delane</div>
        <div class="person__title">Director</div>
      </div>
      <div class="divider"></div>
      <ul class="contacts">
        <li>
          <svg viewBox="0 0 10 10" aria-hidden="true"><path d="M2 1 L4 1 L4.6 3 L3.6 3.8 Q4.6 5.6 6.2 6.4 L7 5.4 L9 6 L9 8 Q5 9 2.5 6 Q1 4 2 1 Z" fill="#1f3c7e"/></svg>
          (555) 014-2290
        </li>
        <li>
          <svg viewBox="0 0 10 10" aria-hidden="true"><rect x="0.8" y="2" width="8.4" height="6" fill="none" stroke="#1f3c7e" stroke-width="1"/><path d="M0.8 2 L5 5.4 L9.2 2" fill="none" stroke="#1f3c7e" stroke-width="1"/></svg>
          info@corvellbuild.com
        </li>
        <li class="web">
          <svg viewBox="0 0 10 10" aria-hidden="true"><circle cx="5" cy="5" r="4.2" fill="#1f3c7e"/><path d="M0.8 5 H9.2 M5 0.8 V9.2" stroke="#fff" stroke-width="0.6"/><ellipse cx="5" cy="5" rx="2" ry="4.2" fill="none" stroke="#fff" stroke-width="0.6"/></svg>
          www.<span>corvellbuild</span>.com
        </li>
      </ul>
    </div>

    <p class="address">48 Harlow Street Bramford, GA 30999</p>
  </section>

  <section class="card card--back" aria-label="Business card back">
    <div class="wordmark"><span class="wordmark__square"></span>Corvell Construction</div>
    <p class="tagline">I have been in business for 28 years</p>
  </section>
</body>
</html>
```